Flyer for Roadhaven 41Ter - Fresh Food Vending Machine in Helchteren

Project Description:
Roadhaven 41Ter has placed a new fresh food vending machine in Helchteren at KP Sodas (Lindeweg 517). We want to create an eye-catching, modern flyer to inform local residents about this vending machine and invite them to visit. The flyer will be distributed door-to-door in Helchteren.
Target Audience:
Residents of Helchteren and surrounding areas.
People looking for quick, fresh meals such as daily specials, wraps, poke bowls, soups, and pasta dishes.
Key Message:
Main title: "Helchteren, we’re here!"
Location: "Our brand-new fresh food vending machine is now at KP Sodas, Lindeweg 517!"
Available products: "Daily specials, wraps, poke bowls, soups, pasta dishes, and more."
Promotion: "For a limited time: with every product, you’ll receive a scratch card, and you always win!"
Style Guidelines:
Clean, professional, and inviting design.
Follow the new branding style of Roadhaven 41Ter (refer to the most recent posts on our Instagram and Facebook pages). Or see attachment for the layout inspiration.
Instagram: www.pictagram-example.com/roadhaven41ter
Facebook: www.friendbook-example.com/Roadhaven41
Do not use the older branding visible in earlier posts.
Format:
Flyer size: A5 (148 x 210 mm).
Additional Information:
Include our logos and social media accounts on the flyer.
Add a clear call-to-action, such as: "Visit us today!"
Ensure the flyer is easy to read and that all information is clear at a glance.
We look forward to seeing your creative and inspiring designs!

```html
<!DOCTYPE html>
<html lang="en">
<head>
<meta charset="utf-8">
<title>Roadhaven 41Ter – Helchteren Flyer</title>
<link href="https://fonts.googleapis.com/css2?family=Lilita+One&family=Montserrat:ital,wght@0,500;0,700;0,800;0,900;1,700;1,800;1,900&display=swap" rel="stylesheet">
<style>
  :root{
    --page:#ffffff;
    --navy:#1f5f86;
    --navy-deep:#174a6c;
    --teal:#4f9fb8;
    --glow:#d9ec8a;
    --yellow:#f9d423;
    --yellow-deep:#c99a00;
    --white:#ffffff;
    --pink:#f6d9d7;
    --coral:#f2837c;
    --ink:#151515;
    --blue-text:#2b6fa0;
    --red:#e3151a;
    --display:"Lilita One","Arial Black",Impact,sans-serif;
  }
  *{margin:0;padding:0;box-sizing:border-box}
  html,body{width:1200px;height:1200px;overflow:hidden;background:var(--page)}
  .flyer{
    position:absolute;left:198px;top:30px;width:874px;height:1240px;
    transform:scale(.919);transform-origin:0 0;overflow:hidden;
    font-family:"Montserrat",sans-serif;background:var(--pink);
  }
  .hero{
    position:absolute;left:0;top:0;width:874px;height:875px;
    background:
      radial-gradient(ellipse 200px 190px at 70px 520px, rgba(226,236,120,.9), transparent 70%),
      radial-gradient(ellipse 180px 170px at 800px 460px, rgba(226,236,120,.55), transparent 70%),
      radial-gradient(ellipse 220px 180px at 810px 800px, rgba(226,236,120,.8), transparent 70%),
      radial-gradient(ellipse 500px 560px at 437px 420px, #7cc0d6 0%, var(--teal) 42%, var(--navy) 80%, var(--navy-deep) 100%);
  }
  .brand{
    position:absolute;left:712px;top:24px;width:146px;
    font-family:var(--display);font-size:24px;line-height:1;
    color:var(--white);text-align:right;letter-spacing:.5px;
  }
  .headline{
    position:absolute;left:0;width:874px;top:78px;text-align:center;
    font-family:var(--display);font-weight:900;font-size:96px;color:var(--white);
    letter-spacing:3px;line-height:1;text-shadow:0 5px 0 rgba(10,40,60,.45);
  }
  .headline .quote{color:var(--yellow)}
  .subhead{
    position:absolute;left:0;width:874px;top:182px;text-align:center;
    font-family:var(--display);font-weight:900;font-size:64px;color:var(--yellow);line-height:1;
    text-shadow:0 4px 0 rgba(10,40,60,.4);
  }
  .tagline{
    position:absolute;left:0;width:874px;top:276px;text-align:center;
    font-weight:800;font-style:italic;font-size:25px;color:var(--coral);
  }
  .offer-list{
    position:absolute;left:0;width:874px;top:308px;list-style:none;text-align:center;
    color:var(--white);font-weight:700;font-size:18px;line-height:26px;
  }
  .offer-list li::before{content:"•";margin-right:12px}
  .offer-list .rule{display:block;width:520px;height:1px;background:rgba(255,255,255,.45);margin:6px auto 0}
  .art{position:absolute}
  .machine{left:205px;top:385px;width:440px;height:510px;border-radius:32px;
    background:radial-gradient(ellipse at 40% 45%, rgba(120,220,205,.95) 0%, rgba(70,190,180,.85) 45%, rgba(230,120,60,.75) 85%, rgba(230,120,60,0) 100%);
    box-shadow:0 18px 30px rgba(0,0,0,.25)}
  .dish{border-radius:50%;box-shadow:0 8px 14px rgba(0,0,0,.2)}
  .dish-pasta{left:32px;top:432px;width:132px;height:96px;background:radial-gradient(#e9a53b,#d9463a 80%)}
  .dish-poke{left:30px;top:680px;width:126px;height:100px;background:radial-gradient(#f0d27a,#8a4a62 85%)}
  .dish-soup{left:722px;top:390px;width:120px;height:120px;background:radial-gradient(#f4d59c,#d9383a 80%)}
  .dish-wrap{left:712px;top:700px;width:150px;height:90px;border-radius:45%;background:radial-gradient(#8d5a34,#e8c487 80%)}
  .label{
    position:absolute;font-family:var(--display);font-weight:900;color:var(--white);
    font-size:38px;line-height:35px;text-align:center;letter-spacing:1px;
    text-shadow:0 3px 0 rgba(0,0,0,.45);
  }
  .label-pasta{left:20px;top:544px;width:170px}
  .label-poke{left:20px;top:788px;width:170px}
  .label-soup{left:700px;top:528px;width:160px}
  .label-wrap{left:700px;top:802px;width:160px}
  .find-us{position:absolute;left:37px;top:944px}
  .find-us h2{font-weight:800;font-size:27px;color:var(--ink);text-decoration:underline;text-underline-offset:4px;margin-left:4px}
  .find-us address{font-style:normal;font-weight:800;font-size:33px;line-height:35px;color:var(--ink);margin-top:10px}
  .find-us .venue{color:var(--blue-text);font-style:italic}
  .find-us .cta{font-weight:900;font-style:italic;font-size:32px;color:var(--yellow);margin-top:4px;-webkit-text-stroke:1px #5c4300}
  .divider{position:absolute;left:446px;top:965px;width:2px;height:124px;background:var(--ink)}
  .badge{position:absolute;left:472px;top:925px;width:166px;height:186px}
  .badge-text{
    position:absolute;left:472px;top:962px;width:166px;text-align:center;
    font-family:var(--display);font-weight:900;color:var(--red);line-height:1;
  }
  .badge-text .s{font-size:29px;letter-spacing:1px}
  .badge-text .a{font-size:28px;color:var(--ink);margin-top:2px}
  .badge-text .w{font-size:56px;margin-top:0;letter-spacing:3px}
  .promo{position:absolute;left:668px;top:965px;width:200px;font-weight:700;font-size:12.5px;line-height:14px;color:var(--ink)}
  .promo em{color:var(--red);font-style:italic}
  .promo-rule{position:absolute;left:650px;top:1027px;width:224px;height:1px;background:var(--ink)}
  .socials{position:absolute;left:668px;top:1035px;list-style:none;font-weight:700;font-size:12.5px;line-height:14px;color:var(--ink)}
  .socials li{display:flex;gap:8px;align-items:flex-start;margin-bottom:5px}
  .socials .dot{width:18px;height:18px;border:2px solid var(--ink);border-radius:3px;flex:none;margin-top:3px}
  .footer-wave{position:absolute;left:0;top:1150px;width:874px;height:90px}
</style>
</head>
<body>
<main class="flyer">
  <section class="hero">
    <div class="brand">ROADHAVEN<br>41TER</div>
    <h1 class="headline"><span class="quote">''</span>HELCHTEREN<span class="quote">''</span></h1>
    <p class="subhead">WE'RE HERE !</p>
    <p class="tagline">FRESH FOOD VENDING MACHINE</p>
    <ul class="offer-list">
      <li>DAILY SPECIALSWRAPS</li>
      <li>WRAPS, POKE BOWLS, SOUPS, PASTA DISHES &amp; MORE</li>
      <span class="rule"></span>
    </ul>
    <div class="art machine" role="img" aria-label="Colourful fresh food vending machine stocked with meals"></div>
    <div class="art dish dish-pasta" role="img" aria-label="Bowl of pasta"></div>
    <div class="art dish dish-poke" role="img" aria-label="Poke bowl with salmon and vegetables"></div>
    <div class="art dish dish-soup" role="img" aria-label="Noodle soup bowl with chopsticks"></div>
    <div class="art dish dish-wrap" role="img" aria-label="Two filled wraps"></div>
    <p class="label label-pasta">PASTAS</p>
    <p class="label label-poke">POKE<br>BOWLS</p>
    <p class="label label-soup">SOUP<br>BOWLS</p>
    <p class="label label-wrap">WRAPS</p>
  </section>

  <section class="find-us">
    <h2>FIND US</h2>
    <address>AT <span class="venue">KP SODAS</span> ,<br>LINDEWEG 517<br>HELCHTEREN.</address>
    <p class="cta">VISIT US TODAY !"</p>
  </section>

  <div class="divider"></div>

  <svg class="badge" viewBox="0 0 166 186" aria-hidden="true">
    <polygon fill="#f9d423" stroke="#e2b400" stroke-width="2" points="83,2 96,18 116,8 120,30 142,28 136,50 158,60 142,76 160,93 142,110 158,126 136,136 142,158 120,156 116,178 96,168 83,184 70,168 50,178 46,156 24,158 30,136 8,126 24,110 6,93 24,76 8,60 30,50 24,28 46,30 50,8 70,18"/>
  </svg>
  <div class="badge-text">
    <div class="s">SCRATCH</div>
    <div class="a">&amp;</div>
    <div class="w">WIN</div>
  </div>

  <p class="promo">FOR A <em>LIMITED TIME</em>: WITH <em>EVERY PRODUCT</em>, YOU'LL RECEIVE <em>A SCRATCH CARD</em>, AND YOU ALWAYS <em>WIN</em> !</p>
  <div class="promo-rule"></div>
  <ul class="socials">
    <li><span class="dot"></span><span>INSTAGRAM:<br>@ROADHAVEN41TER</span></li>
    <li><span class="dot"></span><span>FACEBOOK:<br>ROADHAVEN41</span></li>
  </ul>

  <svg class="footer-wave" viewBox="0 0 874 90" preserveAspectRatio="none" aria-hidden="true">
    <path fill="#1f5f86" d="M0,50 Q31,0 62,50 Q93,0 124,50 Q155,0 186,50 Q217,0 248,50 Q279,0 310,50 Q341,0 372,50 Q403,0 434,50 Q465,0 496,50 Q527,0 558,50 Q589,0 620,50 Q651,0 682,50 Q713,0 744,50 Q775,0 806,50 Q837,0 874,45 L874,90 L0,90 Z"/>
  </svg>
</main>
</body>
</html>
```